依頼詳細
「企業ロゴ」が黒と黄色のため、基本的なカラーリングベースは、黒色で黄色のあしらいやワンポイントカラーを入れるイメージを持っております。
デザインイメージは、「未来的」「先進的」などを強く主張したいと思っております。

本件は、Topページのみのテストとして、「コンペ形式」となりますが、
当選された場合には、約10ページほどの下層ページのご依頼も約束させて頂きます。
(予算は10万円前後)
さらに、今後の案件にて、「継続的」に案件を斡旋させて頂きたいと思っておりますので、
末長くお付き合いして頂けると幸いです。
また、当選後は、デザインに利用したファイルやデータを提出して頂きたいです。

```html
<!DOCTYPE html>
<html lang="ja">
<head>
<meta charset="utf-8">
<title>Novaline | Web Consulting &amp; Creative</title>
<link rel="stylesheet" href="https://fonts.googleapis.com/css2?family=Libre+Baskerville:wght@400;700&family=Noto+Serif+JP:wght@400;600;700&display=swap">
<style>
:root{
  --ink:#0d0d0f;
  --gold:#e0b84a;
  --gold-deep:#b8892a;
  --gold-pale:#f3d98a;
  --paper:#f4f1ea;
  --muted:#c9c6bf;
  --serif-en:"Libre Baskerville", "Noto Serif JP", serif;
  --serif-jp:"Noto Serif JP", serif;
}
*{box-sizing:border-box;margin:0;padding:0}
html,body{width:1200px;height:4504px;overflow:hidden}
body{background:var(--ink);color:var(--paper);font-family:var(--serif-jp);position:relative}
section,header,footer{position:absolute;left:0;width:1200px;overflow:hidden}
.abs{position:absolute}
.btn{position:absolute;display:flex;align-items:center;justify-content:center;height:50px;padding:0 34px;white-space:nowrap;
  background:linear-gradient(180deg,var(--gold-pale),var(--gold) 55%,var(--gold-deep));color:var(--ink);
  font-size:19px;font-weight:600;border-radius:4px;box-shadow:0 2px 0 #6d5214}
.btn.small{height:40px;font-size:16px;padding:0 22px}
.photo{position:absolute}

/* header + hero */
.hero{top:0;height:680px;background:var(--ink)}
.hero-visual{left:0;top:0;width:1200px;height:680px;
  background:radial-gradient(circle at 78% 38%,rgba(255,80,140,.55),transparent 30%),
  radial-gradient(circle at 62% 55%,rgba(60,170,255,.5),transparent 35%),
  radial-gradient(circle at 30% 30%,rgba(255,200,60,.45),transparent 40%),
  linear-gradient(180deg,#2b2a18,#16140c 60%,#0d0d0f)}
.brand{position:absolute;left:160px;top:30px;display:flex;align-items:center;gap:12px}
.brand-name{font-family:var(--serif-en);font-size:40px;font-weight:700;color:var(--paper)}
.brand-mark{width:30px;height:30px;background:var(--gold)}
.global-nav{position:absolute;left:520px;top:44px;display:flex;gap:26px;font-family:var(--serif-en);font-size:28px;color:var(--paper)}
.hero-title{position:absolute;left:120px;top:200px;font-family:var(--serif-en);font-size:50px;line-height:1.3;color:#fff;font-weight:400}
.hero-lead{position:absolute;left:120px;top:412px;font-size:24px;line-height:1.4;color:var(--gold-pale)}
.hero-points{position:absolute;left:120px;top:462px;font-family:var(--serif-en);font-size:22px;line-height:1.65;color:#fff}

/* news */
.news{top:680px;height:300px;background:linear-gradient(180deg,#1e1e22,#141417)}
.news-title{left:340px;top:36px;font-family:var(--serif-en);font-size:44px;letter-spacing:2px;padding-bottom:6px;border-bottom:2px solid var(--paper)}
.news-list{left:230px;top:120px;list-style:none}
.news-item{display:flex;align-items:center;gap:18px;height:58px;font-size:24px}
.news-date{display:flex;align-items:center;gap:6px;font-family:var(--serif-en);color:var(--gold)}
.news-date small{font-size:14px;color:var(--paper)}
.news-date b{font-size:38px;font-weight:700}
.news-tag{font-size:15px;color:var(--muted)}

/* about */
.about{top:980px;height:820px;background:linear-gradient(180deg,#2d2d33,#1c1c20 50%,#26262b)}
.about-head{top:56px;width:100%;text-align:center;font-size:34px;line-height:1.6;font-weight:600}
.about-body{top:190px;left:100px;width:1000px;text-align:center;font-size:17px;line-height:1.85;color:var(--paper)}
.about-body p+p{margin-top:20px}

/* services */
.services{top:1800px;height:1240px;background:linear-gradient(180deg,#1a1a1d,#222226 50%,#121214)}
.services-title{left:760px;top:60px;font-family:var(--serif-en);font-size:50px;letter-spacing:3px}
.services-rule{left:560px;top:132px;width:640px;height:3px;background:var(--gold)}
.svc-heading{position:absolute;font-size:30px;font-weight:600}
.svc-text{position:absolute;font-size:17px;line-height:1.9;color:var(--paper)}

/* banner */
.banner{top:3040px;height:620px}
.banner-visual{left:0;top:0;width:1200px;height:620px;
  background:radial-gradient(circle at 70% 40%,#5a4f3e,transparent 45%),radial-gradient(circle at 35% 30%,#4a3a2c,transparent 40%),linear-gradient(180deg,#3a3630,#1a1916)}
.banner-title{left:0;top:34px;width:1200px;text-align:center;font-size:32px;font-weight:700;color:#fff;white-space:nowrap}
.banner-body{left:260px;top:130px;width:640px;text-align:center;font-size:19px;line-height:2}
.banner-body p+p{margin-top:22px}

/* cta */
.cta{top:3660px;height:610px;background:linear-gradient(180deg,#1a1c1e,#24282a 50%,#121314)}
.cta-head{top:44px;width:100%;text-align:center;font-size:40px;line-height:1.5;font-weight:600}
.cta-body{top:180px;left:150px;width:900px;text-align:center;font-size:16px;line-height:1.8}
.cta-body p+p{margin-top:14px}

/* footer */
.site-footer{top:4270px;height:234px;background:var(--ink)}
.footer-nav{top:8px;width:100%;display:flex;justify-content:center;gap:30px;font-family:var(--serif-en);font-size:32px}
.footer-sub{top:62px;width:100%;display:flex;justify-content:center;gap:30px;font-family:var(--serif-en);font-size:28px}
.footer-brand{left:420px;top:128px;display:flex;align-items:center;gap:12px}
.copyright{left:700px;top:146px;font-size:16px;color:var(--muted)}
</style>
</head>
<body>

<header class="hero">
  <div class="abs hero-visual" role="img" aria-label="Neon-lit city street at night with a glowing, multicolored wolf head"></div>
  <div class="brand"><span class="brand-name">Novaline</span><span class="brand-mark"></span></div>
  <nav class="global-nav"><span>Services</span><span>Company</span><span>News</span><span>Contact</span><span>Recruit</span></nav>
  <h1 class="hero-title">Achieve Online Success<br>with Digital Marketing<br>Professionals!</h1>
  <p class="hero-lead">デジタルマーケティングのプロと共にオンラインの成功を</p>
  <p class="hero-points">Transforming Business with Digital Innovation<br>Leading Businesses<br>Cutting-Edge Web Consulting and Creative Excellence</p>
</header>

<section class="news">
  <h2 class="abs news-title">NEWS</h2>
  <ul class="abs news-list">
    <li class="news-item"><span class="news-date"><small>2023.4</small><b>03</b></span><span class="news-tag">お知らせ</span><span>記事タイトル記事タイトル記事タイトル。</span></li>
    <li class="news-item"><span class="news-date"><small>2023.4</small><b>10</b></span><span class="news-tag">お知らせ</span><span>記事タイトル記事タイトル記事タイトル。</span></li>
    <li class="news-item"><span class="news-date"><small>2023.4</small><b>22</b></span><span class="news-tag">お知らせ</span><span>記事タイトル記事タイトル記事タイトル。</span></li>
  </ul>
</section>

<section class="about">
  <h2 class="abs about-head">デジタル革命をリードする<br>Webコンサルティングと制作のプロフェッショナル</h2>
  <div class="abs about-body">
    <p>当社は、革新的なWebコンサルティングと卓越した制作力を結集し、<br>お客様のビジネスを次のレベルに引き上げるお手伝いをしています。<br>私たちはデジタルの世界において、競争力を高め、<br>オンラインでの成功を実現するための最適なソリューションを提供しています。</p>
    <p>デジタル時代において、ウェブはビジネスの顔となり、<br>オンラインプレゼンスは成功を左右します。<br>私たちはデザインの美しさとパフォーマンスの最適化を両立させ、<br>魅力的で使いやすいウェブサイトを実現します。ユーザーエクスペリエンスを重視し、<br>ユーザーのニーズに応えるインタラクティブなデザインを提供することで、<br>顧客の心をつかみ、ビジネスの成果を最大化します。</p>
    <p>私たちのチームは、経験豊富な専門家から成り立っており、<br>最新のトレンドやテクノロジーに常にアンテナを張っています。<br>クライアントのビジョンと目標を理解し、戦略的かつ創造的なアプローチでプロジェクトに取り組みます。<br>プロジェクトの成功は私たちの成功でもあり、<br>常に最高の品質と顧客満足度を追求することをお約束いたします。</p>
  </div>
  <span class="btn" style="left:510px;top:744px">View More</span>
</section>

<section class="services">
  <h2 class="abs services-title">SERVICE</h2>
  <div class="abs services-rule"></div>

  <h3 class="svc-heading" style="left:240px;top:180px">Web制作</h3>
  <p class="svc-text" style="left:240px;top:235px;width:350px">オンライン空間におけるあなたのビジネスの顔となるWeb制作は、私たちの得意分野です。デザインの美しさと使いやすさを両立し、ブランドの魅力を最大限に引き出すサイトを制作いたします。</p>
  <span class="btn small" style="left:240px;top:420px">制作実績はこちら</span>
  <div class="photo" role="img" aria-label="Hands typing on a laptop with glowing holographic data" style="left:640px;top:150px;width:420px;height:250px;background:linear-gradient(135deg,#2e3440,#6d7684 60%,#9aa3ae)"></div>

  <div class="photo" role="img" aria-label="Man in a suit touching a glowing purple digital interface" style="left:220px;top:470px;width:380px;height:280px;background:radial-gradient(circle at 70% 40%,#b46cff,transparent 50%),linear-gradient(135deg,#1b1440,#3d2c7a)"></div>
  <h3 class="svc-heading" style="left:690px;top:570px">フリーランス支援</h3>
  <p class="svc-text" style="left:640px;top:625px;width:380px">私たちは、フリーランスとして活躍する皆様を全力で支援します。案件の紹介から契約、プロジェクト管理まで、安心してお仕事に集中できる環境をご提供いたします。</p>
  <span class="btn small" style="left:740px;top:790px">お客様の声はこちら</span>

  <h3 class="svc-heading" style="left:220px;top:860px">イベント企画・運営</h3>
  <p class="svc-text" style="left:220px;top:915px;width:300px">私たちはイベントの企画から運営まで一貫してサポートします。参加者の心に残る体験をデザインし、ブランドの価値を高めます。</p>
  <span class="btn small" style="left:220px;top:1130px">イベント一覧へ</span>
  <div class="photo" role="img" aria-label="Person silhouetted against a large illuminated city screen" style="left:530px;top:840px;width:330px;height:250px;background:linear-gradient(160deg,#0e3b66,#2b7fc4 55%,#0b1a2c)"></div>
  <span class="btn small" style="left:540px;top:1130px">お客様の声はこちら</span>
  <div class="photo" role="img" aria-label="White howling wolf silhouette" style="left:870px;top:900px;width:200px;height:260px;background:radial-gradient(ellipse at 50% 55%,#e9e9e9,#8a8a8a 60%,transparent 72%)"></div>
</section>

<section class="banner">
  <div class="abs banner-visual" role="img" aria-label="Businessman in a suit beside a wolf in a dim forest"></div>
  <h2 class="abs banner-title">革新的なWebコンサルティング・制作会社で共に未来を創造しませんか</h2>
  <div class="abs banner-body">
    <p>当社は、デジタル領域での先進的なソリューションを提供し、<br>顧客の成功を支えるリーディングカンパニーです。<br>私たちのチームは、クリエイティブな挑戦が好きな人材が集まり、<br>革新的なアイデアで業界をリードしています。</p>
    <p>私たちのチームは、<br>チャレンジ精神に溢れ、柔軟な考え方を大切にしています。<br>革新的なアイデアを生み出し、<br>デザインの美しさとパフォーマンスの最適化を<br>両立させることに情熱を持って取り組んでいます。</p>
  </div>
  <span class="btn" style="left:880px;top:540px">View More</span>
</section>

<section class="cta">
  <h2 class="abs cta-head">革新的なウェブソリューションで<br>ビジネスを次のレベルへ</h2>
  <div class="abs cta-body">
    <p>私たちのWebコンサルティング・制作チームは、<br>デジタルマーケティングでの成功を追求する情熱と豊富なノウハウを有しております。<br>お客様のビジネスにおいて、オンラインプレゼンスの向上、<br>顧客エンゲージメントの増大、売上の拡大を実現する最適な手法をご提案いたします。</p>
    <p>私たちの特徴は、<br>デザインの美しさとパフォーマンスの最適化を両立させることです。<br>また、デジタルマーケティングのエキスパートとして、<br>常に、オンライン成功のための最新技術やトレンドを取り入れています。</p>
    <p>まずはお気軽にお問い合わせフォームからご連絡ください。<br>お客様のビジネスに合わせた最適なソリューションをご提案いたします。<br>お問い合わせをお待ちしております。</p>
  </div>
  <span class="btn" style="left:470px;top:535px">お問い合わせはこちら</span>
</section>

<footer class="site-footer">
  <nav class="abs footer-nav"><span>Services</span><span>Company</span><span>News</span><span>Contact</span><span>Recruit</span></nav>
  <div class="abs footer-sub"><span>Site Map</span><span>Privacy Policy</span></div>
  <div class="abs footer-brand"><span class="brand-name">Novaline</span><span class="brand-mark"></span></div>
  <p class="abs copyright">© Copyright 株式会社Novaline</p>
</footer>

</body>
</html>
```